BLUE HAVEN (Business Card for Training Company)

Blue Haven is a training and consultancy company with a focus on executive protection and medical. I would like the card to be nice and sharp, not overdone and in black and red. I would also like it to highlight that it is "A Dravin Company"

I would like it to be simple and highlight a few things.

1. Name
2. Title
3. Phone Number
4. Email

I would also like www.dravinholdings.example/blue-haven to be on the card somewhere.

Target Market(s)

Security Companies

Industry/Entity Type

Security

Contact Information for Business Card

Blue Haven is a training and consultancy company with a focus on executive protection and medical. I would like the card to be nice and sharp, not overdone and in black and red. I would also like it to highlight that it is "A Dravin Company" I would like it to be simple and highlight a few things. 1. Name 2. Title 3. Phone Number 4. Email I would also like www.dravinholdings.example/blue-haven to be on the card somewhere.

Requirements
Must have
• A Dravin Company listed on the card and the website
Nice to have
• Highlight Medical Training, Consultancy & Executive Protection Courses

```html
<!DOCTYPE html>
<html lang="en">
<head>
<meta charset="utf-8">
<title>Blue Haven — Business Card</title>
<link rel="stylesheet" href="https://fonts.googleapis.com/css2?family=Open+Sans:ital,wght@0,400;0,600;0,700;0,800;1,400&display=swap">
<style>
  :root {
    --page: #2a2a2a;
    --card: #141414;
    --red: #8e1419;
    --white: #f2f2f2;
    --ghost: #2c2c2c;
    --muted: #bdbdbd;
  }
  * { margin: 0; padding: 0; box-sizing: border-box; }
  html, body { width: 1200px; height: 900px; overflow: hidden; background: var(--page); }
  body {
    font-family: "Open Sans", sans-serif;
    display: flex; flex-direction: column; align-items: center; justify-content: center; gap: 40px;
  }
  .card {
    position: relative; width: 700px; height: 400px; background: var(--card);
    border-bottom: 7px solid var(--red);
    box-shadow: 0 14px 30px rgba(0,0,0,.55);
    overflow: hidden;
  }
  /* Front */
  .brand-name {
    position: absolute; left: 60px; top: 120px;
    font-weight: 800; font-size: 46px; line-height: 1.05; color: var(--white); letter-spacing: 1px;
  }
  .divider {
    position: absolute; left: 330px; top: 100px; width: 1px; height: 200px; background: var(--red);
  }
  .contact { position: absolute; left: 360px; top: 118px; }
  .person-name { color: var(--red); font-weight: 700; font-size: 26px; text-transform: uppercase; letter-spacing: .5px; }
  .person-title { color: var(--white); font-style: italic; font-size: 19px; margin-bottom: 14px; }
  .contact-line { display: flex; align-items: center; gap: 10px; color: var(--white); font-size: 18px; line-height: 1.55; }
  .contact-line svg { width: 14px; height: 14px; fill: var(--red); flex: none; }
  /* Back */
  .ghost-name {
    position: absolute; right: 50px; top: 50px; text-align: right;
    font-weight: 800; font-size: 90px; line-height: .95; color: var(--ghost);
  }
  .parent { position: absolute; left: 50px; bottom: 70px; color: var(--red); font-weight: 600; font-size: 17px; text-transform: uppercase; letter-spacing: .5px; }
  .services { position: absolute; left: 50px; bottom: 30px; color: var(--white); font-size: 19px; }
  .services .dot { color: var(--red); margin: 0 8px; }
</style>
</head>
<body>
  <section class="card card-front">
    <div class="brand-name">BLUE<br>HAVEN</div>
    <div class="divider"></div>
    <div class="contact">
      <div class="person-name">Jaren Colter</div>
      <div class="person-title">President</div>
      <div class="contact-line">
        <svg viewBox="0 0 24 24" aria-hidden="true"><path d="M6.6 10.8a15 15 0 0 0 6.6 6.6l2.2-2.2c.3-.3.7-.4 1-.2 1.1.4 2.3.6 3.6.6.6 0 1 .4 1 1V20c0 .6-.4 1-1 1A17 17 0 0 1 3 4c0-.6.4-1 1-1h3.5c.6 0 1 .4 1 1 0 1.3.2 2.5.6 3.6.1.3 0 .7-.2 1z"/></svg>
        555-013-4782
      </div>
      <div class="contact-line">
        <svg viewBox="0 0 24 24" aria-hidden="true"><path d="M2 5h20v14H2z M2 5l10 8 10-8" /></svg>
        info@dravinholdings.example
      </div>
      <div class="contact-line">
        <svg viewBox="0 0 24 24" aria-hidden="true"><circle cx="12" cy="12" r="10"/></svg>
        www.dravinholdings.example/blue-haven
      </div>
    </div>
  </section>

  <section class="card card-back">
    <div class="ghost-name">BLUE<br>HAVEN</div>
    <div class="parent">A Dravin Company</div>
    <div class="services">Medical Training<span class="dot">•</span>Consultancy<span class="dot">•</span>Executive Protection Courses</div>
  </section>
</body>
</html>
```